Modern Corporate Brochure For Australian Real Estate Agency

We need a corporate 10 page A4 brochure for a Australian Real Estate agency with information for our clients and referral partners.

Main colour scheme: #238b53

Examples of designs:
https://plorvendax.example/item/8-page-corporate-business-brochure/5820417

https://plorvendax.example/item/brochure/7461283

https://plorvendax.example/item/the-company-profile/39851620

https://plorvendax.example/item/brochure-pack-a4trifold-leafletbusiness-card/857312

Target Market(s)

Professional Australians

Industry/Entity Type

Real Estate

Font styles to use
Sans Serif

Requirements
Must have
• Use of multiple greens from the logo

```html
<!DOCTYPE html>
<html lang="en">
<head>
<meta charset="utf-8">
<title>Halvern Property Group – Brochure Cover</title>
<link rel="stylesheet" href="https://fonts.googleapis.com/css2?family=Jost:ital,wght@0,400;0,500;0,700;1,400;1,700&display=swap">
<style>
  :root {
    --green: #238b53;
    --green-deep: #17703f;
    --green-bright: #3bab5f;
    --page-grey: #e6e7e9;
    --paper: #ffffff;
    --ink: #1f2a24;
    --backdrop: #8a8283;
    --sky: #2f6fc8;
    --sky-light: #6aa5e6;
    --lawn: #6f9a3c;
  }
  * { box-sizing: border-box; margin: 0; padding: 0; }
  html, body { width: 900px; height: 1200px; overflow: hidden; }
  body {
    background: var(--backdrop);
    font-family: "Jost", "Helvetica Neue", Arial, sans-serif;
    position: relative;
  }
  .spread {
    position: absolute;
    left: 77px;
    top: 360px;
    width: 746px;
    height: 481px;
    box-shadow: 0 4px 14px rgba(0,0,0,0.35);
    overflow: hidden;
  }
  .spread-shapes { position: absolute; inset: 0; }
  .testimonial {
    position: absolute;
    left: 22px; top: 198px; width: 330px;
    text-align: center;
    font-size: 7.2px; line-height: 1.35;
    font-style: italic;
    color: var(--ink);
  }
  .testimonial-author {
    margin-top: 6px;
    font-weight: 700;
    color: var(--green-deep);
    letter-spacing: 0.2px;
  }
  .brand {
    position: absolute;
    display: flex; align-items: center; gap: 6px;
    font-weight: 500;
    color: var(--green-deep);
    white-space: nowrap;
  }
  .brand-mark { display: block; background: var(--green); }
  .brand--front { left: 390px; top: 70px; font-size: 12px; }
  .brand--front .brand-mark { width: 11px; height: 11px; }
  .brand--back { left: 14px; top: 453px; font-size: 10px; }
  .brand--back .brand-mark { width: 9px; height: 9px; }
  .contact {
    position: absolute;
    left: 224px; top: 437px;
    color: #fff;
  }
  .contact-phone { font-size: 11px; font-weight: 700; letter-spacing: 0.2px; }
  .contact-social {
    margin-top: 4px;
    display: flex; align-items: center; gap: 3px;
    font-size: 7.5px; letter-spacing: 0.3px;
  }
  .contact-social .dot {
    width: 13px; height: 13px; border-radius: 50%; background: #fff; display: inline-block;
  }
  .contact-social .label { margin-right: 4px; }
  .intro { position: absolute; left: 387px; color: #fff; white-space: nowrap; }
  .intro-tagline { top: 316px; font-size: 12.5px; font-weight: 700; line-height: 1.1; letter-spacing: 0.2px; }
  .intro-tagline span { display: block; font-weight: 500; }
  .intro-title { top: 361px; font-size: 14.5px; font-weight: 700; letter-spacing: 0.2px; }
  .intro-body { font-size: 7.2px; line-height: 1.3; font-weight: 400; }
  .intro-body--one { top: 381px; }
  .intro-body--two { top: 414px; }
  .intro-web {
    top: 458px;
    font-size: 7.6px;
    display: flex; align-items: center; gap: 4px;
  }
  .intro-web strong { font-weight: 700; }
  .intro-web .dot { width: 7px; height: 7px; border-radius: 50%; background: #fff; display: inline-block; }
</style>
</head>
<body>
  <section class="spread" aria-label="Brochure cover spread">
    <svg class="spread-shapes" viewBox="0 0 746 481" width="746" height="481">
      <defs>
        <linearGradient id="greenPanel" x1="0" y1="0" x2="1" y2="1">
          <stop offset="0" stop-color="var(--green-bright)"/>
          <stop offset="0.55" stop-color="var(--green)"/>
          <stop offset="1" stop-color="var(--green-deep)"/>
        </linearGradient>
        <linearGradient id="greenBack" x1="0" y1="0" x2="1" y2="0">
          <stop offset="0" stop-color="var(--green-deep)"/>
          <stop offset="1" stop-color="var(--green)"/>
        </linearGradient>
        <linearGradient id="photoTones" x1="0" y1="0" x2="0" y2="1">
          <stop offset="0" stop-color="var(--sky)"/>
          <stop offset="0.45" stop-color="var(--sky-light)"/>
          <stop offset="0.72" stop-color="#3e4c6e"/>
          <stop offset="1" stop-color="var(--lawn)"/>
        </linearGradient>
      </defs>
      <rect class="page-back" x="0" y="0" width="373" height="481" fill="var(--page-grey)"/>
      <rect class="page-front" x="373" y="0" width="373" height="481" fill="var(--paper)"/>
      <polygon class="panel-green-back" points="373,213 373,481 175,481" fill="url(#greenBack)"/>
      <polygon class="panel-green-front" points="373,222 457,222 716,481 373,481" fill="url(#greenPanel)"/>
      <rect class="accent-diamond" x="386" y="180" width="30" height="30" fill="var(--green-bright)" transform="rotate(45 401 195)"/>
      <polygon class="photo-house" role="img" aria-label="Photo of a two-storey blue weatherboard house with white trim, stone retaining wall and garden under a clear blue sky"
        points="670,0 746,0 746,430 713,463 460,210" fill="url(#photoTones)"/>
    </svg>

    <blockquote class="testimonial">
      <p>Great agents, prompt, professional and some of the easiest to deal with people in the industry. After 12 months at Wrenfield, I couldn't recommend their friendly team more. Appreciate all your administration and making life easy.</p>
      <p class="testimonial-author">DALTON PREECE – TENANT REVIEW</p>
    </blockquote>

    <div class="brand brand--front"><span class="brand-mark"></span>HALVERN PROPERTY GROUP</div>
    <div class="brand brand--back"><span class="brand-mark"></span>HALVERN PROPERTY GROUP</div>

    <div class="contact">
      <p class="contact-phone">Call Us: (07) 5550 0142</p>
      <p class="contact-social"><span class="label">FOLLOW US ON</span><span class="dot"></span><span class="dot"></span><span class="dot"></span></p>
    </div>

    <h2 class="intro intro-tagline">FORWARD THINKING<span>PROPERTY SPECIALISTS</span></h2>
    <h1 class="intro intro-title">HALVERN PROPERTY GROUP</h1>
    <p class="intro intro-body intro-body--one">one of Queensland's fastest growing property management<br>specialists In just seven years we now collectively manage almost<br>a billion dollars of residential assets along Queensland's coastline.</p>
    <p class="intro intro-body intro-body--two">Our specialist teams in Brisbane &amp; Gladstone are focused on delivering<br>superior results and better service than any other agency in the market<br>place for both owners and tenants.</p>
    <p class="intro intro-web"><span class="dot"></span>www.<strong>halvernproperty</strong>.example</p>
  </section>
</body>
</html>
```